Banner Design for High End Jewelry Website

We need a banner for our website (brivela.com) for a sale that we will be running. The banner should be a size 1187 × 400. I have included a few pieces of jewelry to be included in the banner (do not need to use all, can use just some). The banner should say:
"Christmas is Closer Than You Think Sale!"
Shop Now

Industry/Entity Type

Jewelry

```html
<!DOCTYPE html>
<html lang="en">
<head>
<meta charset="utf-8">
<title>Christmas Sale Banner</title>
<link rel="stylesheet" href="https://fonts.googleapis.com/css2?family=Tinos&display=swap">
<style>
  :root {
    --page-bg: #f4f4f4;
    --banner-bg: #fdeef1;
    --headline: #8c7262;
    --button-bg: #d63a4b;
    --button-text: #ffffff;
    --gold-light: #e9dc9a;
    --gold-mid: #cdb45a;
    --gem-deep: #8a5a4a;
  }
  * { margin: 0; padding: 0; box-sizing: border-box; }
  html, body {
    width: 1200px;
    height: 1200px;
    overflow: hidden;
    background: var(--page-bg);
  }
  .canvas {
    position: relative;
    width: 1200px;
    height: 1200px;
  }
  .sale-banner {
    position: absolute;
    left: 0;
    top: 398px;
    width: 1200px;
    height: 404px;
    background: var(--banner-bg);
  }
  .sale-copy {
    position: absolute;
    left: 180px;
    top: 104px;
    width: 400px;
    text-align: center;
    font-family: "Tinos", "Times New Roman", serif;
    color: var(--headline);
  }
  .sale-headline {
    font-weight: 400;
    font-size: 42px;
    line-height: 43px;
    letter-spacing: -1px;
    text-transform: uppercase;
    white-space: nowrap;
  }
  .sale-headline span {
    display: block;
    transform: scaleX(0.8);
    transform-origin: center;
  }
  .shop-button {
    position: absolute;
    left: 119px;
    top: 148px;
    width: 163px;
    height: 42px;
    line-height: 44px;
    background: var(--button-bg);
    color: var(--button-text);
    font-family: "Tinos", "Times New Roman", serif;
    font-size: 30px;
    letter-spacing: -1px;
    text-decoration: none;
    text-transform: uppercase;
    text-align: center;
    white-space: nowrap;
  }
  .shop-button span {
    display: inline-block;
    transform: scaleX(0.85);
  }
  .product-photo {
    position: absolute;
    left: 705px;
    top: 66px;
    width: 365px;
    height: 320px;
    border-radius: 18px;
    background: linear-gradient(180deg, var(--gold-light) 0%, var(--gold-mid) 45%, var(--gem-deep) 70%, var(--banner-bg) 100%);
    opacity: 0.55;
  }
</style>
</head>
<body>
  <main class="canvas">
    <section class="sale-banner">
      <div class="sale-copy">
        <h1 class="sale-headline">
          <span>"Christmas is closer</span>
          <span>than you</span>
          <span>think sale!"</span>
        </h1>
        <a class="shop-button" href="#"><span>Shop Now</span></a>
      </div>
      <div class="product-photo" role="img" aria-label="Product photo: pair of gold figure-eight earrings set with diamonds, a green cabochon and a ruby cabochon, with a soft reflection below"></div>
    </section>
  </main>
</body>
</html>
```